New Infusion Pharmacy needs Business Card design

Hello!

We are Verant Infusion Pharmacy, are we are looking for a two sided, clean and modern business card.

First, let me give you a little bit about what an infusion pharmacy does...
We compound and fill prescriptions for drugs that are injectable, meaning that they are administered via an IV bag or a syringe. Basically anything that is too advanced for a normal pill pharmacy to fill. We compound everything in our state of the art clean room, then deliver it directly to the patients home. We have an outside sales force that markets to hospitals, home health agencies, and doctor's offices.

as for the business card...
We are looking for a clean, modern card. our colors are in our logo, kind of a light bule and a darker blue. We do really like the rounded corners on the card. Also, we would like the back of the card to be the reverse colors of the front, for example, if the front of the card has a light background, then the back of the card will have a dark background.

On the back side of the card we want to have our logo, then list some of the services we offer:
-IVIG
-TPN
-Enteral Nutrition
-IV Antibiotics
-IV Hydration
-Blood Factors
-Chemotherapy
-Pain Management

Our logo is uploaded in .psd format, if you need a different format let me know and i'll throw it up here.

Thank you so much!!

Industry/Entity Type

Pharmacy

Requirements
Must have
• Front of Card: (no particular order, please arrange in whatever way you think looks best!)
-Employee Name
-Title
-Office Phone #
-Cell Phone #
-Fax #
-email address - marlo@verantcareinfuse.com
-office address - 4127 Delmore St. Cypress, CA 90630
-Web Site - www.verantcareinfuse.com

```html
<!DOCTYPE html>
<html lang="en">
<head>
<meta charset="utf-8">
<title>Verant Infusion Pharmacy – Business Card</title>
<link href="https://fonts.googleapis.com/css2?family=Source+Sans+3:wght@400;600&display=swap" rel="stylesheet">
<style>
  :root {
    --backdrop: #e9e6e2;
    --paper: #ffffff;
    --navy-teal: #0f5a72;
    --teal: #1686a6;
    --sky: #2aa7cf;
    --teal-glow: #1fa2c2;
    --teal-edge: #0b5f74;
    --ink: #5a6670;
    --rule: #b9bfc4;
    --white: #ffffff;
  }
  * { margin: 0; padding: 0; box-sizing: border-box; }
  html, body { width: 1200px; height: 836px; overflow: hidden; }
  body {
    background: var(--backdrop);
    font-family: "Source Sans 3", "Myriad Pro", sans-serif;
    position: relative;
  }
  .card {
    position: absolute;
    width: 540px;
    height: 310px;
    border-radius: 26px;
    overflow: hidden;
    box-shadow: 0 8px 22px rgba(0,0,0,.22);
  }

  /* Front */
  .card-front { left: 580px; top: 80px; background: var(--paper); }
  .front-brand {
    position: absolute; right: 40px; top: 44px;
    color: var(--teal); font-weight: 600; font-size: 26px; letter-spacing: .5px;
  }
  .front-rule {
    position: absolute; left: 32px; right: 40px; top: 150px;
    height: 1px; background: var(--rule);
  }
  .front-details { position: absolute; left: 40px; top: 168px; color: var(--ink); font-size: 14px; line-height: 20px; }
  .person { font-size: 17px; color: var(--ink); margin-bottom: 4px; }
  .person .name { color: var(--navy-teal); font-weight: 600; }
  .line { display: flex; align-items: center; gap: 5px; white-space: nowrap; }
  .line svg { width: 13px; height: 13px; fill: none; stroke: var(--navy-teal); stroke-width: 1.6; }
  .line .gap { width: 8px; }
  .swoosh { position: absolute; left: 0; bottom: 0; width: 540px; height: 110px; }

  /* Back */
  .card-back {
    left: 80px; top: 440px;
    background: radial-gradient(ellipse at 40% 35%, var(--teal-glow) 0%, var(--teal) 45%, var(--teal-edge) 100%);
    color: var(--white); text-align: center;
  }
  .back-brand {
    margin-top: 52px;
    color: var(--navy-teal); font-weight: 600; font-size: 30px; letter-spacing: .5px;
  }
  .services-title {
    display: inline-block; margin-top: 18px;
    font-size: 18px; text-decoration: underline; text-underline-offset: 3px;
  }
  .services {
    display: flex; justify-content: center; gap: 36px;
    margin-top: 8px; text-align: left; font-size: 15px; line-height: 19px; list-style: none;
  }
  .services ul { list-style: none; }
  .services li::before { content: "* "; }
  .services .col-left { margin-top: 22px; }
  .website { position: absolute; left: 0; right: 0; bottom: 26px; font-size: 16px; }
</style>
</head>
<body>

<section class="card card-front" aria-label="Card front">
  <div class="front-brand">Verant Infusion Pharmacy</div>
  <div class="front-rule"></div>
  <div class="front-details">
    <p class="person"><span class="name">Your Name :</span> Designation</p>
    <p class="line">4127 Delmore St. Cypress, CA 90630</p>
    <p class="line">
      <svg viewBox="0 0 14 14"><rect x="4" y="1" width="6" height="12" rx="1"/></svg>(714) 555-0142
      <span class="gap"></span>
      <svg viewBox="0 0 14 14"><path d="M3 2 L6 2 L7 5 L5 6 Q6 9 8 10 L9 8 L12 9 L12 12 Q5 12 3 2 Z"/></svg>(714) 555-0187
      <span class="gap"></span>
      <svg viewBox="0 0 14 14"><rect x="2" y="6" width="10" height="6"/><rect x="4" y="2" width="6" height="4"/></svg>(714) 555-0193
    </p>
    <p class="line">
      <svg viewBox="0 0 14 14"><rect x="1.5" y="3" width="11" height="8"/><path d="M1.5 3 L7 8 L12.5 3"/></svg>marlo@verantcareinfuse.com
    </p>
  </div>
  <svg class="swoosh" viewBox="0 0 540 110" preserveAspectRatio="none" aria-hidden="true">
    <path d="M0 78 Q270 96 540 6 L540 110 L0 110 Z" fill="var(--sky)"/>
    <path d="M0 88 Q280 104 540 16 L540 110 L0 110 Z" fill="var(--paper)"/>
    <path d="M0 94 Q300 108 540 22 L540 110 L0 110 Z" fill="var(--navy-teal)"/>
  </svg>
</section>

<section class="card card-back" aria-label="Card back">
  <div class="back-brand">Verant Infusion Pharmacy</div>
  <h2 class="services-title">SERVICES WE OFFER</h2>
  <div class="services">
    <ul class="col-left">
      <li>IVIG</li>
      <li>Enteral Nutrition</li>
      <li>IV Hydration</li>
      <li>Chemotherapy</li>
    </ul>
    <ul class="col-right">
      <li>TPN</li>
      <li>IV Antibiotics</li>
      <li>Blood Factors</li>
      <li>Pain Management</li>
    </ul>
  </div>
  <p class="website">www.verantcareinfuse.com</p>
</section>

</body>
</html>
```